Corvane Project Services - Flyer

Project Breif:
I need a single page A4 Capability Statement, which will be used to market our services to prospective clients, both in print and via email PDF.
It needs to look professional and should incorporate the elements I have uploaded into files, these include:
Capability Statement Text
Corvane Services Company Logo
Additional Logo’s (Tools We Use)
Glimmer Bay Pics can be cut into the page
I have included examples of capability statements as a guide to what i am looking for.
Regards
Derek
Engineering Consulting

```html
<!DOCTYPE html>
<html lang="en">
<head>
<meta charset="utf-8">
<title>Corvane Project Services – Capability Statement</title>
<link href="https://fonts.googleapis.com/css2?family=Poppins:wght@300;400;600;700&display=swap" rel="stylesheet">
<style>
  :root {
    --navy: #0d4a8a;
    --navy-deep: #0a3f78;
    --sky: #8dcdea;
    --sky-light: #bfe2f3;
    --rule: #2c6fae;
    --white: #ffffff;
    --ink: #0b3b6e;
    --grey: #6a6a6a;
  }
  * { box-sizing: border-box; margin: 0; padding: 0; }
  html, body { width: 860px; height: 1200px; overflow: hidden; }
  body { font-family: "Poppins", Arial, sans-serif; background: var(--white); }

  .flyer { position: relative; width: 860px; height: 1200px; background: var(--navy); overflow: hidden; }

  .masthead { position: absolute; left: 0; top: 0; width: 860px; height: 168px; background: var(--white); }
  .brand { position: absolute; left: 42px; top: 40px; width: 200px; text-align: center; }
  .brand-mark { width: 70px; height: 70px; border-radius: 50%; background: var(--navy); margin: 0 auto 8px; }
  .brand-name { font-size: 14px; font-weight: 600; color: var(--navy-deep); letter-spacing: 0.5px; line-height: 1.25; }

  .person { position: absolute; right: 39px; top: 38px; text-align: right; }
  .person-name { font-size: 38px; font-weight: 700; color: var(--navy); line-height: 1.1;
                 border-bottom: 2px solid var(--navy); padding-bottom: 2px; }
  .person-role { font-size: 17px; font-weight: 400; color: var(--navy); margin-top: 4px; }

  .contact-bar { position: absolute; left: 385px; right: 0; top: 141px; height: 26px; background: var(--sky-light);
                 font-size: 12px; color: var(--navy); display: flex; align-items: center; padding-left: 14px; gap: 6px; }

  .hero { position: absolute; left: 21px; top: 168px; width: 818px; height: 403px;
          background: linear-gradient(115deg, #d9dee4 0%, #f3f5f7 40%, #e3e8ee 70%, #c9d2dc 100%); }

  .about { position: absolute; left: 41px; top: 580px; width: 380px; color: var(--white); }
  .about h2 { font-size: 25px; font-weight: 700; color: var(--sky-light); border-bottom: 2px solid var(--sky);
              padding-bottom: 2px; margin-bottom: 14px; width: 378px; }
  .about p { font-size: 14.2px; font-weight: 300; line-height: 1.36; margin-bottom: 18px; }

  .schedule-shot { position: absolute; left: 41px; top: 885px; width: 380px; height: 212px;
                   background: linear-gradient(180deg, #eef2f6 0%, #dbe3ec 100%); }

  .services { position: absolute; left: 444px; top: 488px; width: 377px; height: 613px; background: var(--sky); }
  .services-title { background: var(--navy); color: var(--white); font-size: 25px; font-weight: 600;
                    height: 46px; display: flex; align-items: center; padding-left: 8px; margin: 2px 2px 0; }
  .service-group { padding: 0 12px 0 8px; margin-top: 10px; }
  .service-group h3 { font-size: 17px; font-weight: 600; color: var(--ink); border-bottom: 1.5px solid var(--rule);
                      padding-bottom: 1px; margin-bottom: 4px; }
  .service-group ul { list-style: none; }
  .service-group li { font-size: 15px; color: var(--ink); line-height: 26px; padding-left: 18px; position: relative; }
  .service-group li::before { content: ""; position: absolute; left: 3px; top: 10px; width: 8px; height: 8px; background: var(--navy); }

  .toolbar { position: absolute; left: 0; top: 1112px; width: 860px; height: 88px; background: var(--white);
             display: flex; align-items: center; justify-content: space-around; padding: 0 20px; }
  .tool { font-size: 14px; font-weight: 600; color: var(--navy-deep); display: flex; align-items: center; gap: 6px; }
  .tool-dot { width: 12px; height: 12px; background: var(--navy-deep); }
</style>
</head>
<body>
<main class="flyer">
  <header class="masthead">
    <div class="brand">
      <div class="brand-mark"></div>
      <div class="brand-name">CORVANE PROJECT SERVICES</div>
    </div>
    <div class="person">
      <div class="person-name">Derek Halloran</div>
      <div class="person-role">(Managing Director)</div>
    </div>
    <div class="contact-bar">
      <span>info@corvaneservices.ie</span><span>|</span><span>www.corvaneservices.ie</span><span>|</span><span>+353 (0)870005142</span>
    </div>
  </header>

  <div class="hero" role="img" aria-label="Photo of a team meeting with hands holding printed charts and reports over a table"></div>

  <section class="about">
    <h2>About Us:</h2>
    <p>Corvane Project Services Ltd. is a leading project control consultancy based in Co Cork Ireland. For over 20 years we have been helping our clients to deliver complex projects and programs throughout mainland Europe.</p>
    <p>We are passionate about empower organisations to achieve their objectives, on time and on budget.</p>
    <p>We are continually innovating, evolving and learning, utilize the latest industry tools and techniques to deliver real value to our clients.</p>
  </section>

  <div class="schedule-shot" role="img" aria-label="Screenshot of a project schedule Gantt chart with coloured task bars"></div>

  <section class="services">
    <div class="services-title">Core Services:</div>
    <div class="service-group">
      <h3>Planning and Scheduling</h3>
      <ul>
        <li>Tender Planning</li>
        <li>Interactive Planning / Pull Planning</li>
        <li>EPCMV Planning &amp; Scheduling</li>
        <li>Schedule Earned Value Management</li>
        <li>Independent Schedule Quality Assessment</li>
        <li>Schedule Risk Analysis (Monte Carlo)</li>
        <li>Training</li>
      </ul>
    </div>
    <div class="service-group">
      <h3>Management of Risk</h3>
      <ul>
        <li>Risk Management Policies &amp; Procedures</li>
        <li>Risk Management Strategy</li>
        <li>Risk Registers</li>
        <li>Risk Improvement Planning</li>
        <li>Risk Response and Communication</li>
        <li>Risk Management Training</li>
      </ul>
    </div>
    <div class="service-group">
      <h3>Cost Control</h3>
      <ul>
        <li>Estimating &amp; Forecasting</li>
        <li>Earned Value Analysis</li>
        <li>Progress Reporting</li>
        <li>Cost Risk Analysis</li>
      </ul>
    </div>
  </section>

  <footer class="toolbar">
    <span class="tool"><span class="tool-dot"></span>Meridian Scheduler</span>
    <span class="tool">Taskline</span>
    <span class="tool">Keystone Planner</span>
    <span class="tool">Waypoint Pro</span>
    <span class="tool">Ledgerly Gauge</span>
    <span class="tool">Riskwise</span>
  </footer>
</main>
</body>
</html>
```